Medical device box for kits used for self testing purposes. Attractive simplistic design

Looking for a design that will go on a box that offer multiple range of medical testing ranging from hormones panel to diabetes and thyroid hormones. looking for something attractive and simple to go on a box 6 x 4.5 x 1 inches. attached are some examples from competitors. and our logo that be incorporated with the design.
Picture of the boxes have been attached, pick the color you think goes best with your design.

Target Market(s)

Patients and regular consumers

Industry/Entity Type

Medical

Requirements
Nice to have
• Simple design that is eye catching

```html
<!DOCTYPE html>
<html lang="en">
<head>
<meta charset="utf-8">
<title>Hormones Panel – Box Front</title>
<link href="https://fonts.googleapis.com/css2?family=Noto+Sans:wght@700&display=swap" rel="stylesheet">
<style>
  :root {
    --ink: #111a3a;
    --paper: #ffffff;
    --frame: #6e6e6e;
    --wave-mid: #3267b7;
    --wave-light: #78a6d9;
    --wave-deep: #223c68;
  }
  html, body {
    margin: 0;
    padding: 0;
    width: 1200px;
    height: 922px;
    overflow: hidden;
    background: var(--paper);
  }
  .box-front {
    position: relative;
    width: 1200px;
    height: 922px;
    font-family: "Noto Sans", "DejaVu Sans", sans-serif;
  }
  .box-front__frame {
    position: absolute;
    left: 6px;
    top: 2px;
    width: 1187px;
    height: 907px;
    border: 2px solid var(--frame);
    box-sizing: border-box;
    overflow: hidden;
  }
  .wave-art {
    position: absolute;
    left: 0;
    top: 0;
    width: 100%;
    height: 100%;
  }
  .brand {
    position: absolute;
    left: 80px;
    top: 78px;
    display: flex;
    align-items: center;
    gap: 14px;
    color: var(--ink);
    font-weight: 700;
    font-size: 62px;
    line-height: 1;
    letter-spacing: 1px;
  }
  .brand__dot {
    width: 48px;
    height: 48px;
    border-radius: 50%;
    background: var(--ink);
  }
  .product-title {
    position: absolute;
    left: 82px;
    top: 460px;
    margin: 0;
    color: var(--ink);
    font-weight: 700;
    font-size: 67px;
    line-height: 67px;
    letter-spacing: 2px;
  }
</style>
</head>
<body>
  <main class="box-front">
    <div class="box-front__frame">
      <svg class="wave-art" viewBox="0 0 1365 1023" preserveAspectRatio="none" role="img" aria-label="Layered blue wave decoration">
        <defs>
          <linearGradient id="wave-fill" x1="0" y1="0" x2="1" y2="0.4">
            <stop offset="0" stop-color="var(--wave-mid)"/>
            <stop offset="0.55" stop-color="var(--wave-light)"/>
            <stop offset="1" stop-color="var(--wave-deep)"/>
          </linearGradient>
        </defs>
        <g transform="translate(-8,-2)">
          <path fill="url(#wave-fill)" d="M133,1025 C220,915 330,840 490,827 C780,805 930,760 1030,520 C1130,300 1260,245 1375,232 L1375,1030 L133,1030 Z"/>
        </g>
      </svg>
    </div>

    <div class="brand">
      <span class="brand__dot"></span>
      <span class="brand__name">Novira</span>
    </div>

    <h1 class="product-title">Hormones<br>Panel</h1>
  </main>
</body>
</html>
```